Frostwyn.co - Polar Expeditions Specialists

We need a modern, visually striking business card for Frostwyn.co, a company specialized in selling expedition cruises to the most remote regions on Earth, with a focus on the Arctic and Antarctica. The design should instantly communicate that the cardholder is an expert in polar travel. Use clean, premium aesthetics with cool tones like icy blue and white, possibly incorporating polar imagery (ice, glaciers, penguins, etc.)

Attached the logo

Contact Information for Business Card

Feels high-end and trustworthy.. Visually memorable — encourages people to keep it

Colors
0054AA
0677BA
7BADD7
CADEEF
E8F1F8

Requirements
Must have
• ice, glaciers, penguins, montains
Nice to have
• modern, transparente,

```html
<!DOCTYPE html>
<html lang="en">
<head>
<meta charset="utf-8">
<title>Frostwyn.co – Business Card</title>
<link href="https://fonts.googleapis.com/css2?family=Poppins:wght@600;800&family=Montserrat:wght@400;700&display=swap" rel="stylesheet">
<style>
  :root {
    --backdrop: #1c1d20;
    --card: #151516;
    --edge: #3479c0;
    --brand-blue: #3479c0;
    --silver: #c9c9c9;
    --text-light: #f2f2f2;
    --text-muted: #8e8e8e;
  }
  * { box-sizing: border-box; margin: 0; padding: 0; }
  html, body { width: 1200px; height: 840px; overflow: hidden; background: var(--backdrop); }
  .canvas { position: relative; width: 1200px; height: 840px; }

  .card {
    position: absolute;
    left: 320px;
    width: 560px;
    height: 320px;
    background: var(--card);
    border-radius: 22px;
    box-shadow: 0 4px 0 var(--edge), 0 18px 40px rgba(0,0,0,.5);
    overflow: hidden;
  }
  .card--front { top: 70px; }
  .card--back { top: 440px; }

  /* Front side */
  .front-brand {
    position: absolute; inset: 0;
    display: flex; align-items: center; justify-content: center; gap: 18px;
  }
  .brand-dot { width: 46px; height: 46px; border-radius: 50%; background: var(--silver); }
  .front-brand .brand-name {
    font-family: "Poppins", sans-serif; font-weight: 800; font-size: 52px;
    color: var(--silver); line-height: 1; letter-spacing: -0.5px;
  }
  .front-brand .brand-tagline {
    font-family: "Poppins", sans-serif; font-weight: 600; font-size: 15px;
    color: var(--text-muted); margin-top: 6px;
  }

  /* Back side */
  .holder { position: absolute; top: 26px; right: 30px; text-align: right; }
  .holder-name {
    font-family: "Montserrat", sans-serif; font-weight: 700; font-size: 26px;
    color: var(--brand-blue); letter-spacing: 0.5px; line-height: 1.1;
  }
  .holder-role {
    font-family: "Montserrat", sans-serif; font-weight: 400; font-size: 13px;
    color: var(--text-light); margin-top: 2px;
  }
  .holder-bar { position: absolute; top: 20px; right: 0; width: 10px; height: 44px; background: var(--brand-blue); }

  .back-brand { position: absolute; top: 104px; left: 30px; display: flex; align-items: center; gap: 10px; }
  .back-brand .brand-dot { width: 30px; height: 30px; background: var(--brand-blue); }
  .back-brand .brand-name {
    font-family: "Poppins", sans-serif; font-weight: 800; font-size: 30px;
    color: var(--brand-blue); line-height: 1;
  }
  .back-brand .brand-tagline {
    font-family: "Poppins", sans-serif; font-weight: 600; font-size: 10px;
    color: var(--brand-blue); margin-top: 3px;
  }

  .contact { position: absolute; left: 70px; bottom: 28px; font-family: "Montserrat", sans-serif; color: var(--text-light); }
  .contact-address { font-size: 13px; line-height: 1.45; margin-bottom: 14px; }
  .contact-list { list-style: none; font-size: 13px; line-height: 1.6; }
  .contact-list li { display: flex; align-items: center; gap: 8px; }
  .contact-list svg { width: 12px; height: 12px; fill: var(--brand-blue); flex: none; }

  .polar-artwork { position: absolute; right: 24px; bottom: 0; width: 220px; height: 196px; }
</style>
</head>
<body>
<main class="canvas">

  <section class="card card--front" aria-label="Card front">
    <div class="front-brand">
      <span class="brand-dot"></span>
      <div>
        <div class="brand-name">Frostwyn.co</div>
        <div class="brand-tagline">Polar Expeditions Specialists</div>
      </div>
    </div>
  </section>

  <section class="card card--back" aria-label="Card back">
    <span class="holder-bar"></span>
    <div class="holder">
      <div class="holder-name">ELIAS MARSH</div>
      <div class="holder-role">Managing Director</div>
    </div>

    <div class="back-brand">
      <span class="brand-dot"></span>
      <div>
        <div class="brand-name">Frostwyn.co</div>
        <div class="brand-tagline">Polar Expeditions Specialists</div>
      </div>
    </div>

    <div class="contact">
      <p class="contact-address">Your address, City<br>State, Zip 1234</p>
      <ul class="contact-list">
        <li><svg viewBox="0 0 12 12"><path d="M2.5 1 4.5 3 3.6 4.4a7 7 0 0 0 4 4L9 7.5l2 2-1.3 1.6C5.6 11 1 6.4 .9 2.3z"/></svg>123 456 789</li>
        <li><svg viewBox="0 0 12 12"><path d="M0 2h12v8H0zM1 3v.4l5 3.2 5-3.2V3z"/></svg>info@yourmailbox.com</li>
        <li><svg viewBox="0 0 12 12"><circle cx="6" cy="6" r="5.5"/></svg>www.yourwebsite.com</li>
      </ul>
    </div>

    <svg class="polar-artwork" viewBox="0 0 220 196" role="img" aria-label="Blue silhouette illustration of a polar bear with two penguins and small stars">
      <rect x="0" y="0" width="220" height="220" rx="40" fill="var(--brand-blue)"/>
    </svg>
  </section>

</main>
</body>
</html>
```